Postcard Design

I am an attorney in Pittsburgh. Here and across country, companies are sending data with names, address and new criminal charges for people. This has resulted in some people getting 12 or more of these letters. I want to do a postcard because one does not need to open a postcard. I also want to be delicate since there is no sealed envelope. I want to throw in other matters other than criminal so it does not look like the person is necessarily charged with a crime.
At top would be "Law Office of Dorian F. Haslbeck"
Then:
Need an Attorney?
Attorney Dorian F. Haslbeck has 25 Years of Experience
Free Consultation - Affordable Fees - Credit Cards Accepted
-All Criminal Matters
-Most Civil Matters
-DUI / Traffic Citations / License Restoration
412-555-0187
www.lakesidedefenselawyer.example
www.dfhcounsel.example

My CTQ ranking is A+ but I am not sure they give a logo with the rating. I have all my logos at www.lakesidedefenselawyer.example The purpose of the two websites is these are postcards. I want no one to think oh this person is charged with a crime.

Industry/Entity Type

Attorney

```html
<!DOCTYPE html>
<html lang="en">
<head>
<meta charset="utf-8">
<title>Law Office of Dorian F. Haslbeck – Postcard</title>
<link rel="stylesheet" href="https://fonts.googleapis.com/css2?family=Oswald:wght@500;600;700&family=Cinzel:wght@400;600&family=Roboto+Condensed:ital,wght@0,400;0,700;1,700&family=Arimo&display=swap">
<style>
  :root{
    --navy:#1d2a4f;
    --red:#c81d25;
    --deep-red:#7a1414;
    --orange:#e8902f;
    --black:#1b1b1b;
    --cream:#f8f3e6;
    --paper:#fbf8f0;
    --ink:#222;
    --rule:#5a5a5a;
    --line:#2c3560;
    --photo-warm-1:#f2c27a;
    --photo-warm-2:#8a3d12;
    --photo-blue-1:#5d6f8e;
    --photo-blue-2:#1f2a3d;
  }
  *{box-sizing:border-box;margin:0;padding:0}
  html,body{width:1200px;height:750px;overflow:hidden;background:#e9e6df}
  .canvas{position:relative;width:1200px;height:750px}
  .card{position:absolute;width:570px;height:370px;overflow:hidden;box-shadow:0 4px 14px rgba(0,0,0,.25)}
  .card--front{left:15px;top:190px;background:var(--navy)}
  .card--back{left:615px;top:190px;background:var(--paper)}

  /* front */
  .front-photo{position:absolute;left:0;top:0}
  .front-office{position:absolute;left:22px;top:16px;font-family:'Cinzel',serif;font-size:27px;color:var(--orange);letter-spacing:1px}
  .front-name{position:absolute;left:20px;top:44px;font-family:'Oswald',sans-serif;font-weight:600;font-size:44px;color:#fff;letter-spacing:1px;line-height:1}
  .band-red{position:absolute;left:0;top:112px;width:570px;height:50px;background:var(--red);border-top:4px solid #fff}
  .band-red span{position:absolute;left:22px;top:1px;font-family:'Roboto Condensed',sans-serif;font-style:italic;font-weight:700;font-size:38px;color:#fff}
  .band-black{position:absolute;left:0;top:162px;width:570px;height:38px;background:var(--black);border-bottom:3px solid #fff}
  .band-black span{position:absolute;left:40px;top:3px;font-family:'Oswald',sans-serif;font-weight:500;font-size:24px;color:#fff;letter-spacing:.5px}
  .services{position:absolute;left:0;top:200px;width:570px;height:96px;background:var(--cream);border-bottom:4px solid var(--red);display:flex;gap:24px;padding:12px 22px}
  .services ul{list-style:none}
  .services li{display:flex;align-items:center;gap:7px;font-family:'Oswald',sans-serif;font-weight:500;font-size:14.5px;color:var(--black);line-height:18px;text-transform:uppercase}
  .tick{width:16px;height:16px;flex:none}
  .front-scene{position:absolute;left:0;top:300px;width:570px;height:70px;background:linear-gradient(100deg,var(--photo-blue-2),var(--photo-blue-1) 55%,#c9c3b8)}

  /* back */
  .back-photo{position:absolute;left:0;top:0}
  .tab-office{position:absolute;left:150px;top:24px;height:34px;width:210px;background:var(--red);clip-path:polygon(0 0,93% 0,100% 100%,0 100%);font-family:'Oswald',sans-serif;font-weight:600;font-size:24px;color:#fff;padding:0 0 0 20px;line-height:34px;letter-spacing:.5px}
  .tab-name{position:absolute;left:150px;top:60px;height:42px;width:315px;background:var(--navy);clip-path:polygon(0 0,95% 0,100% 100%,0 100%);font-family:'Oswald',sans-serif;font-weight:600;font-size:29px;color:#fff;padding:0 0 0 20px;line-height:42px;letter-spacing:.5px}
  .postage{position:absolute;left:480px;top:12px;width:80px;height:80px;border:1.5px solid var(--ink);background:#fff;display:flex;align-items:center;justify-content:center;text-align:center;font-family:'Arimo',sans-serif;font-size:11px;line-height:13px;color:var(--ink)}
  .contact{position:absolute;left:160px;top:116px;width:186px}
  .contact-name{font-family:'Cinzel',serif;font-size:17px;color:var(--deep-red);border-bottom:1px solid var(--rule);padding-bottom:2px;white-space:nowrap}
  .contact-rows{margin-top:12px;font-family:'Roboto Condensed',sans-serif;font-size:8.2px;line-height:11px;color:var(--ink)}
  .row{display:flex;margin-bottom:6px}
  .row dt{width:42px;color:var(--deep-red)}
  .row dd{text-transform:uppercase}
  .accent{color:var(--deep-red)}
  .contact-rule{position:absolute;left:160px;top:270px;width:186px;border-top:1px solid var(--rule)}
  .badges{position:absolute;left:164px;top:281px;display:flex;gap:15px;align-items:center}
  .badge-round{width:44px;height:44px;border-radius:50%}
  .badge-round--navy{background:var(--navy);border:3px solid #c7a35a}
  .badge-round--gold{background:#c7a35a;border:3px solid var(--navy)}
  .badge-square{width:56px;height:38px;border-radius:3px;background:#1d5a8c}
  .divider{position:absolute;left:353px;top:118px;height:190px;border-left:1px solid var(--rule)}
  .address-box{position:absolute;left:368px;top:118px;width:190px;height:68px;border:1px solid var(--rule);border-radius:6px;background:#fff}
  .address-line{position:absolute;left:368px;width:190px;border-top:1px solid var(--line)}
</style>
</head>
<body>
<main class="canvas">

  <section class="card card--front" aria-label="Postcard front">
    <svg class="front-photo" width="570" height="120" viewBox="0 0 570 120" role="img" aria-label="Photo of brass scales of justice and a gavel">
      <defs>
        <linearGradient id="frontWarm" x1="0" y1="0" x2="1" y2="1">
          <stop offset="0" stop-color="#5a1e0a"/>
          <stop offset=".5" stop-color="var(--photo-warm-2)"/>
          <stop offset="1" stop-color="var(--photo-warm-1)"/>
        </linearGradient>
      </defs>
      <path d="M400 0 Q460 50 500 120 H570 V0 Z" fill="url(#frontWarm)"/>
      <path d="M400 0 Q460 50 500 120" fill="none" stroke="#fff" stroke-width="2"/>
    </svg>
    <p class="front-office">LAW OFFICE OF</p>
    <h1 class="front-name">DORIAN F. HASLBECK</h1>
    <div class="band-red"><span>Need an Attorney?</span></div>
    <div class="band-black"><span>ATTORNEY DORIAN F. HASLBECK</span></div>
    <div class="services">
      <ul>
        <li><svg class="tick" viewBox="0 0 16 16"><path d="M2 9 L6 13 L14 2" fill="none" stroke="var(--red)" stroke-width="3" stroke-linecap="round"/></svg>Free Consultation</li>
        <li><svg class="tick" viewBox="0 0 16 16"><path d="M2 9 L6 13 L14 2" fill="none" stroke="var(--red)" stroke-width="3" stroke-linecap="round"/></svg>Affordable Fees</li>
        <li><svg class="tick" viewBox="0 0 16 16"><path d="M2 9 L6 13 L14 2" fill="none" stroke="var(--red)" stroke-width="3" stroke-linecap="round"/></svg>Credit Cards Accepted</li>
        <li><svg class="tick" viewBox="0 0 16 16"><path d="M2 9 L6 13 L14 2" fill="none" stroke="var(--red)" stroke-width="3" stroke-linecap="round"/></svg>All Criminal Matters</li>
      </ul>
      <ul>
        <li><svg class="tick" viewBox="0 0 16 16"><path d="M2 9 L6 13 L14 2" fill="none" stroke="var(--red)" stroke-width="3" stroke-linecap="round"/></svg>Most Civil Matters</li>
        <li><svg class="tick" viewBox="0 0 16 16"><path d="M2 9 L6 13 L14 2" fill="none" stroke="var(--red)" stroke-width="3" stroke-linecap="round"/></svg>DUI | Traffic Citations</li>
        <li><span class="tick"></span>| License Restoration</li>
      </ul>
    </div>
    <div class="front-scene" role="img" aria-label="Photo of an officer writing a traffic citation"></div>
  </section>

  <section class="card card--back" aria-label="Postcard back">
    <svg class="back-photo" width="200" height="370" viewBox="0 0 200 370" role="img" aria-label="Photo of a wooden gavel and scales of justice">
      <defs>
        <linearGradient id="backWarm" x1="0" y1="0" x2="1" y2="1">
          <stop offset="0" stop-color="var(--photo-warm-1)"/>
          <stop offset=".55" stop-color="var(--photo-warm-2)"/>
          <stop offset="1" stop-color="#3a1606"/>
        </linearGradient>
      </defs>
      <path d="M0 0 H185 Q125 185 185 370 H0 Z" fill="url(#backWarm)"/>
      <path d="M185 0 Q125 185 185 370" fill="none" stroke="var(--deep-red)" stroke-width="4"/>
    </svg>
    <div class="tab-office">LAW OFFICE OF</div>
    <h2 class="tab-name">DORIAN F. HASLBECK</h2>
    <div class="postage">Postage<br>Area</div>

    <div class="contact">
      <p class="contact-name">DORIAN F HASLBECK</p>
      <dl class="contact-rows">
        <div class="row"><dt>Phone:</dt><dd>412-555-0187<br>412-555-0143 <span class="accent">(AFTER 5:00 P.M.)</span></dd></div>
        <div class="row"><dt>Email:</dt><dd>DORIAN@DFH-LAW.EXAMPLE</dd></div>
        <div class="row"><dt>Address:</dt><dd><span class="accent">DORIAN F. HASLBECK,</span> ESQUIRE<br>615 LAKEVIEW AVENUE<br>SUITE 1400<br>PITTSBURGH, PA 15222</dd></div>
      </dl>
    </div>
    <div class="contact-rule"></div>
    <div class="badges">
      <span class="badge-round badge-round--navy" role="img" aria-label="Lawyers association badge"></span>
      <span class="badge-round badge-round--gold" role="img" aria-label="Trial lawyers badge"></span>
      <span class="badge-square" role="img" aria-label="CTQ A+ rating badge"></span>
    </div>

    <div class="divider"></div>
    <div class="address-box"></div>
    <div class="address-line" style="top:212px"></div>
    <div class="address-line" style="top:240px"></div>
    <div class="address-line" style="top:268px"></div>
    <div class="address-line" style="top:296px"></div>
  </section>

</main>
</body>
</html>
```